Motor Vault Website - Part of the Brantley Group

A complimentary website is required for the launch of a 'Motor Vault' - a new service launched by industry renowned BRANTLEY. Motor Vault is an industry-first brand that designs and builds unique subterranean car parks for private residential homes in London and the influential counties within the UK. Please see here the direction of a new BRANTLEY Website - we would like Motor Vault to be complimentary and sit alongside BRANTLEY harmoniously - https://www.brantleyhq.example/brantley-nu-staging Brantley have some images, but whilst more professional images are in production - we have also attached pixmoor photos- named clearly as pixmoor. **Attached files include JPEG, .eps of logo and Brantley library images and Pixmoor Library Images - two versions of logo dependent on background colour. - Website needs to be sleek, chic and masculine.- Colour Palette - Grey/ Black/ White - Same visiual journey as Brantley website- Required areas within the sit include - About Us / Our Work / Contact Page

Target Market(s)

Luxury
Men

Number of Pages Required

2 page

Font styles to use
Sans Serif

Colors
e8e8e8
757575
1b1b1b
000000
9d9d9d
cbcbcb
f5f5f5

Requirements
Must have
• Complimentary of this site - https://www.brantleyhq.example/brantley-nu-staging
Should not have
• Colour

```html
<!DOCTYPE html>
<html lang="en">
<head>
<meta charset="utf-8">
<title>Motor Vault</title>
<link rel="stylesheet" href="https://fonts.googleapis.com/css2?family=Carlito:wght@400;700&family=Open+Sans:wght@300;400;600;700;800&display=swap">
<style>
:root{
  --black:#000000;
  --ink:#1b1b1b;
  --grey-dark:#757575;
  --grey:#9d9d9d;
  --grey-light:#cbcbcb;
  --mist:#e8e8e8;
  --paper:#f5f5f5;
  --white:#ffffff;
}
*{margin:0;padding:0;box-sizing:border-box}
html,body{width:1200px;height:2778px;overflow:hidden;background:var(--white)}
body{position:relative;font-family:'Carlito',sans-serif;color:var(--ink)}
.abs{position:absolute}

/* Hero */
.hero{left:0;top:0;width:1200px;height:578px;background:radial-gradient(ellipse at 60% 45%,#5a5a5a 0%,#2b2b2b 40%,#0d0d0d 100%)}
.hero-shade{left:0;top:0;width:1200px;height:578px;background:linear-gradient(90deg,rgba(0,0,0,.55) 0%,rgba(0,0,0,.1) 60%,rgba(0,0,0,.35) 100%)}
.brand{left:44px;top:28px;display:flex;align-items:center;gap:10px;color:var(--white);font-family:'Open Sans',sans-serif;font-weight:800;font-size:28px;letter-spacing:.5px}
.brand-mark{width:20px;height:20px;background:var(--white)}
.menu{right:44px;top:22px;display:flex;align-items:center;gap:20px;color:var(--white);font-size:19px}
.menu-btn{width:46px;height:46px;border:2px solid var(--white);display:flex;align-items:center;justify-content:center}
.hero-title{left:50px;top:172px;width:640px;color:var(--white);font-family:'Open Sans',sans-serif;font-weight:600;font-size:50px;line-height:60px}
.hero-sub{left:60px;top:296px;width:620px;color:var(--mist);font-size:28px;line-height:40px;padding-left:52px}
.hero-sub::before{content:"";position:absolute;left:0;top:19px;width:38px;height:2px;background:var(--mist)}
.side-nav{left:982px;top:226px;width:218px}
.side-nav li{list-style:none;border-bottom:1px solid rgba(255,255,255,.18);padding:10px 0 10px 22px;position:relative;height:62px}
.side-nav li::before{content:"";position:absolute;left:4px;top:20px;width:7px;height:7px;background:var(--white)}
.side-nav b{display:block;color:var(--white);font-size:14px;font-weight:700;letter-spacing:.5px}
.side-nav span{display:block;color:var(--grey-dark);font-size:12px}
.scroll{left:575px;top:486px;width:50px;text-align:center;color:var(--grey);font-size:11px}
.scroll-mouse{width:22px;height:34px;border:2px solid var(--grey);border-radius:11px;margin:0 auto 6px}
.follow-item{top:536px;color:var(--white);font-size:12px}

/* Tiles */
.tile{top:578px;height:380px}
.tile-photo-a{left:0;width:278px;background:linear-gradient(135deg,#1a1a1a 0%,#5c5c5c 45%,#9d9d9d 55%,#2a2a2a 100%)}
.tile-text{left:278px;width:328px;background:var(--white);padding:44px 52px 0 32px}
.tile-photo-b{left:606px;width:283px;background:linear-gradient(160deg,#2a2a2a 0%,#8a8a8a 35%,#cbcbcb 50%,#4a4a4a 75%,#151515 100%)}
.tile-photo-c{left:889px;width:311px;background:linear-gradient(120deg,#5a5a5a 0%,#2a2a2a 50%,#0f0f0f 100%)}
.tile-h{font-family:'Open Sans',sans-serif;font-weight:700;font-size:31px;line-height:36px;text-transform:uppercase}
.tile-p{margin-top:20px;font-family:'Open Sans',sans-serif;font-weight:700;font-size:15px;line-height:29px;text-transform:uppercase}
.tile-text .tile-p{color:var(--ink)}
.tile-box{left:903px;top:592px;width:278px;height:350px;background:rgba(20,20,20,.92);border:2px solid var(--grey-dark);padding:30px 16px 0 20px;color:var(--white)}

/* About */
.eyebrow{font-size:15px;color:var(--grey-dark);text-transform:uppercase;letter-spacing:.5px}
.about-eyebrow{left:167px;top:1018px}
.about-title{left:167px;top:1046px;width:840px;font-weight:700;font-size:43px;line-height:60px;color:var(--ink)}
.about-copy{left:167px;top:1232px;width:870px;font-size:16px;line-height:25px;color:var(--grey)}
.feature{width:380px}
.feature-head{display:flex;align-items:center;gap:16px;font-weight:700;font-size:22px;color:var(--ink)}
.feature-num{width:30px;height:30px;border-radius:50%;background:var(--grey-dark);color:var(--white);font-size:15px;display:flex;align-items:center;justify-content:center}
.feature p{margin:6px 0 0 46px;width:300px;font-size:15px;line-height:22px;color:var(--grey)}
.divider{left:167px;top:1758px;width:870px;height:2px;background:var(--grey-light)}

/* Blog */
.blog-eyebrow{left:167px;top:1782px;color:var(--ink);font-weight:700}
.blog-img{top:1834px;width:196px;height:196px}
.blog-img-a{left:167px;background:radial-gradient(circle at 45% 50%,#cbcbcb 0%,#757575 40%,#1b1b1b 80%)}
.blog-img-b{left:628px;background:linear-gradient(150deg,#e8e8e8 0%,#757575 40%,#1b1b1b 70%,#9d9d9d 100%)}
.blog-body{top:1832px;width:190px}
.blog-body h3{font-weight:400;font-size:19px;line-height:24px;color:var(--ink)}
.blog-body p{margin-top:16px;font-size:14px;line-height:20px;color:var(--grey-dark)}

/* Contact footer */
.footer{left:0;top:2075px;width:1200px;height:703px;background:var(--black)}
.footer-eyebrow{color:var(--grey-dark);font-size:13px}
.contact-line{left:167px;top:2150px;width:900px;color:var(--white);font-family:'Open Sans',sans-serif;font-size:44px;line-height:58px;font-weight:400}
.short-rule{left:167px;top:2389px;width:48px;height:2px;background:var(--grey-dark)}
.email{left:167px;top:2432px;color:var(--white);font-family:'Open Sans',sans-serif;font-size:36px}
.tel{left:167px;top:2482px;color:var(--grey-dark);font-size:22px;letter-spacing:.5px}
.address{left:167px;top:2606px;color:var(--grey-dark);font-size:24px;line-height:32px}
.signup{left:675px;top:2617px;display:flex}
.signup-field{width:255px;height:44px;background:#111111}
.signup-btn{width:103px;height:44px;background:var(--ink);color:var(--grey-dark);font-size:13px;display:flex;align-items:center;justify-content:center}
.copyright{left:167px;top:2728px;color:var(--grey-dark);font-size:11px}
</style>
</head>
<body>

<section class="hero abs" role="img" aria-label="Dim underground concrete car park with columns receding into the distance"></section>
<div class="hero-shade abs"></div>

<header>
  <div class="brand abs"><span class="brand-mark"></span>MOTOR VAULT</div>
  <div class="menu abs">Menu
    <span class="menu-btn"><svg width="16" height="14" viewBox="0 0 16 14"><rect y="0" width="16" height="2" fill="#fff"/><rect y="6" width="16" height="2" fill="#fff"/><rect y="12" width="16" height="2" fill="#fff"/></svg></span>
  </div>
</header>

<h1 class="hero-title abs">A carving cave where your vehical can take rest</h1>
<p class="hero-sub abs">Specialising turnkey solutions for Basements, Shell &amp; Core and Interior Fit-Out</p>

<ul class="side-nav abs">
  <li><b>ABOUT</b><span>Who we are</span></li>
  <li><b>BLOG</b><span>Whats New</span></li>
  <li><b>CONTACT</b><span>get in touch</span></li>
</ul>

<div class="scroll abs"><div class="scroll-mouse"></div>Scroll down</div>

<span class="follow-item abs" style="left:54px">Follow Us</span>
<span class="follow-item abs" style="left:144px">Friendbook</span>
<span class="follow-item abs" style="left:203px">Chirper</span>
<span class="follow-item abs" style="left:246px">Linkwork</span>

<section class="tiles">
  <div class="tile tile-photo-a abs" role="img" aria-label="Black and white photo of a lit underground garage corridor"></div>
  <div class="tile tile-text abs">
    <h2 class="tile-h">Residential Basements</h2>
    <p class="tile-p">Under existing London properties, Brantley can create single or double depth basements to provide extra living space for a multitude of uses. We can also provide</p>
  </div>
  <div class="tile tile-photo-b abs" role="img" aria-label="Black and white photo of steel construction framework from below"></div>
  <div class="tile tile-photo-c abs" role="img" aria-label="Dark photo of a building construction site"></div>
  <div class="tile-box abs">
    <h2 class="tile-h">Construction &amp; Design</h2>
    <p class="tile-p">We provide complete project management services to support buildings and basement constructions projects. Works include:</p>
  </div>
</section>

<section class="about">
  <p class="eyebrow about-eyebrow abs">/ Who we are</p>
  <h2 class="about-title abs">It is a long established fact that a reader will be distracted by the readable content of a page when looking at its layout.</h2>
  <p class="about-copy abs">Lorem Ipsum is simply dummy text of the printing and typesetting industry. Lorem Ipsum has been the industry's standard dummy text ever since the 1500s, when an unknown printer took a galley of type and scrambled it to make a type specimen book. It has survived not only five centuries, but also the leap into electronic typesetting, remaining essentially unchanged. It was popularised in the 1960s with the release of Typeline sheets containing Lorem Ipsum passages, and more recently with desktop publishing software like Folio Layout including versions of Lorem Ipsum.</p>

  <div class="feature abs" style="left:167px;top:1382px">
    <div class="feature-head"><span class="feature-num">1</span>What is Lorem Ipsum</div>
    <p>Lorem Ipsum is simply dummy text of the printing and typesetting industry. Lorem Ipsum has been the industry's standard dummy text ever since the 1500s, when an unknown printer took a galley of type and scrambled it</p>
  </div>
  <div class="feature abs" style="left:628px;top:1382px">
    <div class="feature-head"><span class="feature-num">2</span>Why do we use it?</div>
    <p>Lorem Ipsum is simply dummy text of the printing and typesetting industry. Lorem Ipsum has been the industry's standard dummy text ever since the 1500s, when an unknown printer took a galley of type and scrambled it</p>
  </div>
  <div class="feature abs" style="left:167px;top:1562px">
    <div class="feature-head"><span class="feature-num">3</span>Define</div>
    <p>Lorem Ipsum is simply dummy text of the printing and typesetting industry. Lorem Ipsum has been the industry's standard dummy text ever since the 1500s, when an unknown printer took a galley of type and scrambled it</p>
  </div>
  <div class="feature abs" style="left:628px;top:1562px">
    <div class="feature-head"><span class="feature-num">4</span>Define</div>
    <p>Lorem Ipsum is simply dummy text of the printing and typesetting industry. Lorem Ipsum has been the industry's standard dummy text ever since the 1500s, when an unknown printer took a galley of type and scrambled it</p>
  </div>
  <div class="divider abs"></div>
</section>

<section class="blog">
  <p class="eyebrow blog-eyebrow abs">/ New at Motor Vault blog</p>
  <div class="blog-img blog-img-a abs" role="img" aria-label="Close-up black and white photo of a car alloy wheel"></div>
  <div class="blog-body abs" style="left:392px">
    <h3>Delivering the power of parity</h3>
    <p>May 27, 2016 – Equal Voices is described as the biggest international development conference on women's and girls' rights and health...</p>
  </div>
  <div class="blog-img blog-img-b abs" role="img" aria-label="Black and white photo of a steel structure"></div>
  <div class="blog-body abs" style="left:853px">
    <h3>Delivering the power of parity</h3>
    <p>May 27, 2016 – Equal Voices is described as the biggest international development conference on women's and girls' rights and health...</p>
  </div>
</section>

<footer class="footer abs"></footer>
<p class="eyebrow footer-eyebrow abs" style="left:167px;top:2118px">/ Contact us</p>
<p class="contact-line abs">Get in touch and let's make something great together. Let's turn your idea on an even greater product.</p>
<div class="short-rule abs"></div>
<p class="email abs">info@motorvault.com</p>
<p class="tel abs">TEL: 0207 555 0142</p>
<p class="eyebrow footer-eyebrow abs" style="left:167px;top:2576px">/ Where to find us</p>
<p class="address abs">48 Harrow Yard, Mews,<br>London, W2 7QX</p>
<p class="eyebrow footer-eyebrow abs" style="left:675px;top:2576px">/ Follow us</p>
<div class="signup abs"><div class="signup-field"></div><div class="signup-btn">Subscribe</div></div>
<p class="copyright abs">Copyright © Motorvault 2015. Terms &amp; Conditions | Privacy Policy</p>

</body>
</html>
```